Plumbing and Fire Protection Consulting Engineering

Business Cards for one person plumbing and fire protection engineering consulting business based in NJ, serving mostly New York City:
RVT Advisory, Plumbing and Fire Protection Engineering
Daniel Korvinsky- President
52-17 Maple Terrace, Glen Rock, NJ 07452
201-486-2173
rvtpipework@mailbox-example.com

Target Market(s)

- Private Building Developers, looking to reduce construction cost
- MEP (Mechanical, Electrical, Plumbing) Design Engineers that have staff shortage, need temporary help, advise, drawings quality control
- Architects that need advise on plumbing or fire protection
- Any of the above that need opinion on disputed construction costs, change orders, construction observation reports

Industry/Entity Type

Business

Contact Information for Business Card

Logo and business card should include (other suggestions welcome):
- A plumbing symbol, like pipe or wrench or similar
- Fire Protection symbol, like fire sprinkler
- Dollar signs $$$$$ in descending font sizes suggesting construction cost reduction as a result of my work. or some other symbol of economic design
- Symbol of engineering
- High rise building(s) or Manhattan skyline on the background, maybe building under construction.
- Maybe a building floor plan design (preferably old, not modern, like in Michelangelo or Gaudi sketches)

Font styles to use
Sans Serif

Colors

Designer to choose colors to be used in the design.

Requirements
Must have
• A card that is unique, unlike any others- like my business is.
• My name, business name, address, phone, email, see description
Nice to have
• Something that suggests 30+ years experience in this field, not sure how to convey this message.
• Maybe my Linkedin picture with Statue of Liberty on the background (attached) is good to have, but i am not sure- not insisting on that.
Should not have
• Symbols that not related to engineering design and construction- like fire truck, funny plumbers figures and symbols, toilets, etc.
• Computer symbols. I am not trying to impress clients with my computer skills, not my selling point

```html
<!DOCTYPE html>
<html lang="en">
<head>
<meta charset="utf-8">
<title>RVT Advisory – Business Card</title>
<link rel="stylesheet" href="https://fonts.googleapis.com/css2?family=Orbitron:wght@600&family=Roboto:wght@400;500;700&display=swap">
<style>
  :root {
    --stage: #2b2b2b;
    --card: #ffffff;
    --brand-blue: #1766c2;
    --deep-blue: #2a3a9c;
    --sky-blue: #0a92db;
    --accent-orange: #f26a21;
    --tagline-orange: #f7941d;
    --title-red: #ef4e23;
    --ink: #161616;
    --ink-soft: #3a3a3a;
    --icon-blue: #2d3a8c;
  }
  * { margin: 0; padding: 0; box-sizing: border-box; }
  html, body { width: 900px; height: 1200px; overflow: hidden; }
  body {
    background: var(--stage);
    font-family: "Roboto", Arial, sans-serif;
    position: relative;
  }
  .card {
    position: absolute;
    left: 83px;
    width: 735px;
    background: var(--card);
    overflow: hidden;
  }
  .card-front { top: 133px; height: 430px; }
  .card-back { top: 640px; height: 428px; }

  .skyline-photo {
    position: absolute; inset: 0;
    background: linear-gradient(180deg, #f4f6f8 0%, #e7eaee 35%, #dcdfe3 70%, #e9ebee 100%);
  }

  .accent-rule {
    position: absolute; left: 0; right: 0; top: 378px; height: 4px;
    background: var(--accent-orange);
  }
  .footer-band {
    position: absolute; left: 0; right: 0; bottom: 0; height: 44px;
    background: linear-gradient(90deg, var(--deep-blue), var(--sky-blue));
  }

  .brand { position: absolute; display: flex; align-items: center; }
  .brand-mark { border-radius: 50%; background: var(--brand-blue); flex: none; }
  .brand-name {
    font-weight: 700; color: var(--brand-blue);
    text-transform: uppercase; line-height: 1; letter-spacing: 0.2px;
  }
  .brand-tagline { line-height: 1; margin-top: 6px; }

  .card-front .brand { left: 45px; top: 62px; }
  .card-front .brand-mark { width: 66px; height: 66px; margin-right: 24px; }
  .card-front .brand-name { font-size: 33px; }
  .card-front .brand-tagline { font-size: 15.5px; color: var(--tagline-orange); font-weight: 500; }

  .person { position: absolute; left: 45px; top: 219px; }
  .person-name { font-size: 21px; font-weight: 500; color: var(--ink); }
  .person-title { font-size: 17px; color: var(--title-red); margin-top: 3px; }

  .contact-list { position: absolute; left: 45px; top: 280px; list-style: none; }
  .contact-item {
    display: flex; align-items: center; height: 25px;
    font-size: 16px; color: var(--ink);
  }
  .contact-icon { width: 16px; height: 16px; margin-right: 7px; flex: none; fill: var(--icon-blue); }

  .experience {
    position: absolute; right: 26px; bottom: 14px;
    font-family: "Orbitron", "Arial", sans-serif; font-weight: 600;
    font-size: 13.5px; letter-spacing: 1.6px; color: #ffffff; line-height: 1;
  }

  .card-back .brand { left: 125px; top: 167px; }
  .card-back .brand-mark { width: 90px; height: 90px; margin-right: 28px; }
  .card-back .brand-name { font-size: 42px; }
  .card-back .brand-tagline { font-size: 19px; color: var(--ink-soft); font-weight: 500; margin-top: 8px; }
</style>
</head>
<body>

<section class="card card-front">
  <div class="skyline-photo" role="img" aria-label="Faded photograph of the Manhattan skyline with high-rise towers"></div>
  <div class="accent-rule"></div>
  <div class="footer-band"></div>

  <div class="brand">
    <span class="brand-mark"></span>
    <div class="brand-text">
      <div class="brand-name">RVT Advisory</div>
      <div class="brand-tagline">Plumbing and Fire Protection Engineering</div>
    </div>
  </div>

  <div class="person">
    <div class="person-name">Daniel Korvinsky</div>
    <div class="person-title">President</div>
  </div>

  <ul class="contact-list">
    <li class="contact-item">
      <svg class="contact-icon" viewBox="0 0 16 16" aria-hidden="true"><path d="M1,6 Q8,0 15,6 L13,8 L11,6.5 L11,5 Q8,4 5,5 L5,6.5 L3,8 Z M4,8 L12,8 L14,14 L2,14 Z"/></svg>
      201-486-2173
    </li>
    <li class="contact-item">
      <svg class="contact-icon" viewBox="0 0 16 16" aria-hidden="true"><path d="M1,3 L15,3 L15,13 L1,13 Z"/><path d="M1.5,3.5 L8,9 L14.5,3.5" fill="none" stroke="#ffffff" stroke-width="1.3"/></svg>
      rvtpipework@mailbox-example.com
    </li>
    <li class="contact-item">
      <svg class="contact-icon" viewBox="0 0 16 16" aria-hidden="true"><path d="M8,0.5 C4.6,0.5 2.5,3 2.5,6 C2.5,10 8,15.5 8,15.5 C8,15.5 13.5,10 13.5,6 C13.5,3 11.4,0.5 8,0.5 Z M8,3.8 A2.2,2.2 0 1 1 8,8.2 A2.2,2.2 0 1 1 8,3.8 Z"/></svg>
      52-17 Maple Terrace, Glen Rock, NJ 07452 USA
    </li>
  </ul>

  <div class="experience">30+ YEARS EXPERIENCE</div>
</section>

<section class="card card-back">
  <div class="brand">
    <span class="brand-mark"></span>
    <div class="brand-text">
      <div class="brand-name">RVT Advisory</div>
      <div class="brand-tagline">Plumbing and Fire Protection Engineering</div>
    </div>
  </div>
</section>

</body>
</html>
```